Mindfulness School for Children -- Business Cards

We're looking for business cards for our school directors and owners. We're a mindfulness school for children called tumbling willows. Attached are our logos/icons.

```html
<!DOCTYPE html>
<html lang="en">
<head>
<meta charset="utf-8">
<title>tumbling willows – business cards</title>
<link rel="stylesheet" href="https://fonts.googleapis.com/css2?family=Karla:wght@400;700&display=swap">
<style>
  :root {
    --backdrop: #2a2a2c;
    --card-dark: #2f2f30;
    --card-light: #ffffff;
    --teal: #2fa3b7;
    --teal-deep: #2693a8;
    --sea-green: #98d3aa;
    --mark-teal: #4db3c4;
    --text-light: #ffffff;
  }
  * { margin: 0; padding: 0; box-sizing: border-box; }
  html, body {
    width: 1200px; height: 874px; overflow: hidden;
    background: var(--backdrop);
    font-family: "Karla", sans-serif;
  }
  .canvas { position: relative; width: 1200px; height: 874px; }
  .card {
    position: absolute; left: 290px; width: 620px; height: 354px;
    border-radius: 18px; overflow: hidden;
  }
  .card--front { top: 63px; background: var(--card-dark); }
  .card--back { top: 457px; background: var(--card-light); }

  .front-brand {
    position: absolute; inset: 0;
    display: flex; align-items: center; justify-content: center; gap: 14px;
  }
  .brand-dot {
    width: 22px; height: 22px; border-radius: 50%;
    background: var(--mark-teal);
  }
  .brand-name {
    font-weight: 400; font-size: 52px; letter-spacing: 0.5px;
    color: var(--mark-teal);
  }

  .back-brand {
    position: absolute; left: 58px; top: 60px;
    display: flex; align-items: center; gap: 12px;
  }
  .back-brand .brand-dot { width: 34px; height: 34px; }
  .back-brand .brand-name { font-size: 34px; }

  .wave { position: absolute; inset: 0; width: 620px; height: 354px; }

  .contact {
    position: absolute; right: 40px; bottom: 22px;
    text-align: right; color: var(--text-light);
    font-size: 13px; line-height: 16px;
  }
  .contact__name { font-weight: 700; font-size: 18px; letter-spacing: 1.5px; line-height: 20px; }
  .contact__title { font-size: 14px; line-height: 17px; margin-bottom: 3px; }
  .contact__address { margin-bottom: 4px; }
  .contact__line { display: flex; justify-content: flex-end; align-items: center; gap: 6px; }
  .contact__icon { width: 11px; height: 11px; fill: var(--text-light); }
</style>
</head>
<body>
<main class="canvas">

  <section class="card card--front" aria-label="Card front">
    <div class="front-brand">
      <span class="brand-dot"></span>
      <span class="brand-name">tumbling willows</span>
    </div>
  </section>

  <section class="card card--back" aria-label="Card back">
    <div class="back-brand">
      <span class="brand-dot"></span>
      <span class="brand-name">tumbling willows</span>
    </div>

    <svg class="wave" viewBox="0 0 620 354" aria-hidden="true">
      <path d="M0 158 C70 220 170 236 300 200 C430 164 540 108 620 112 L620 354 L0 354 Z" fill="var(--sea-green)"/>
      <path d="M0 170 C70 232 170 248 300 212 C430 176 540 120 620 124 L620 354 L0 354 Z" fill="#ffffff"/>
      <path d="M0 176 C70 238 172 254 302 218 C432 182 540 126 620 130 L620 354 L0 354 Z" fill="var(--teal)"/>
      <path d="M0 176 C60 222 150 238 260 218 C170 232 70 222 0 188 Z" fill="var(--teal-deep)" opacity="0.5"/>
    </svg>

    <div class="contact">
      <p class="contact__name">DANIEL REYES</p>
      <p class="contact__title">President</p>
      <p class="contact__address">4120 Alder Creek Road<br>Juneau, Alaska 99801</p>
      <p class="contact__line">555-014-2231
        <svg class="contact__icon" viewBox="0 0 12 12"><path d="M2.5 1 L4.5 1 L5.3 3.5 L4 4.6 C4.7 6 6 7.3 7.4 8 L8.5 6.7 L11 7.5 L11 9.5 C11 10.3 10.3 11 9.5 11 C5 11 1 7 1 2.5 C1 1.7 1.7 1 2.5 1 Z"/></svg></p>
      <p class="contact__line">555-018-7740
        <svg class="contact__icon" viewBox="0 0 12 12"><path d="M3 0.5 H9 V11.5 H3 Z M4 1.5 V9.5 H8 V1.5 Z" fill-rule="evenodd"/></svg></p>
      <p class="contact__line">555-012-3096
        <svg class="contact__icon" viewBox="0 0 12 12"><path d="M3 1 H9 V4 H3 Z M1 5 H11 V10 H9 V8 H3 V10 H1 Z M3.5 9 H8.5 V11.5 H3.5 Z"/></svg></p>
      <p class="contact__line">name@tumblingwillows.com
        <svg class="contact__icon" viewBox="0 0 12 12"><path d="M1 2.5 H11 V9.5 H1 Z M1.6 3 L6 6.5 L10.4 3 Z" fill-rule="evenodd"/></svg></p>
      <p class="contact__line">www.tumblingwillows.com
        <svg class="contact__icon" viewBox="0 0 12 12"><circle cx="6" cy="6" r="5"/></svg></p>
    </div>
  </section>

</main>
</body>
</html>
```